First Aid Training business needs business card design

We would like a double sided business card designed for a first aid training business - Brindlewood First Aid. We provide first aid training and , WHS (work, health and safety) training.

The attached word document contains the key information we would like on each side of the business card.

Final design needs to be delivered in print ready format, along with the original file.

```html
<!DOCTYPE html>
<html lang="en">
<head>
<meta charset="UTF-8">
<title>Brindlewood First Aid – Business Card</title>
<link rel="stylesheet" href="https://fonts.googleapis.com/css2?family=Montserrat:wght@400;500;600;700;800&display=swap">
<style>
  :root {
    --brand-red: #e2231f;
    --brand-red-soft: #ea4a33;
    --ink: #1a1a1a;
    --paper: #ffffff;
    --backdrop: #e9e9ea;
    --card-w: 900px;
    --card-h: 514px;
  }
  * { margin: 0; padding: 0; box-sizing: border-box; }
  html, body {
    width: 1200px; height: 1186px; overflow: hidden;
    background: var(--backdrop);
    font-family: "Montserrat", sans-serif;
  }
  .sheet {
    width: 1200px; height: 1186px;
    display: flex; flex-direction: column; align-items: center; justify-content: center;
    gap: 60px;
  }
  .card {
    position: relative;
    width: var(--card-w); height: var(--card-h);
    border-radius: 34px;
    overflow: hidden;
    box-shadow: 0 6px 20px rgba(0,0,0,.18);
  }

  /* Front – red side */
  .card--front { background: var(--brand-red); color: var(--paper); }
  .front-halo {
    position: absolute; right: -90px; top: -150px;
    width: 520px; height: 520px; border-radius: 50%;
    background: var(--brand-red-soft); opacity: .75;
  }
  .front-content { position: absolute; left: 70px; top: 70px; right: 70px; }
  .wordmark {
    display: flex; align-items: center; gap: 18px; white-space: nowrap;
  }
  .wordmark-dot {
    width: 64px; height: 64px; border-radius: 50%;
    border: 7px solid currentColor; flex: none;
  }
  .wordmark-name {
    font-weight: 700; font-size: 44px; line-height: 1; letter-spacing: .5px;
    text-transform: uppercase;
  }
  .wordmark-name small { display: block; font-size: 22px; font-weight: 700; margin-top: 6px; letter-spacing: 1px; }
  .tagline {
    margin-top: 44px; font-weight: 700; font-size: 26px;
    display: flex; align-items: center; gap: 14px; white-space: nowrap;
  }
  .benefits { list-style: none; margin: 14px 0 0 48px; }
  .benefits li { font-size: 21px; font-weight: 400; line-height: 1.55; position: relative; padding-left: 20px; }
  .benefits li::before {
    content: ""; position: absolute; left: 0; top: 13px;
    width: 7px; height: 7px; border-radius: 50%; background: var(--paper);
  }
  .services { margin-top: 22px; }
  .service { display: flex; align-items: center; gap: 14px; font-weight: 700; font-size: 27px; line-height: 1.45; }
  .bullet-ring { width: 30px; height: 30px; flex: none; }

  /* Back – white side */
  .card--back { background: var(--paper); color: var(--ink); }
  .back-brand {
    position: absolute; left: 56px; top: 280px;
    display: flex; align-items: center; gap: 16px; white-space: nowrap;
  }
  .back-brand .wordmark-dot { border-color: var(--ink); width: 60px; height: 60px; border-width: 6px; }
  .back-brand .wordmark-name { font-size: 33px; color: var(--ink); }
  .back-brand .wordmark-name small { font-size: 16px; margin-top: 5px; }
  .divider {
    position: absolute; left: 462px; top: 120px; width: 2px; height: 220px;
    background: var(--brand-red);
  }
  .contact { position: absolute; left: 492px; top: 132px; white-space: nowrap; }
  .contact-name { color: var(--brand-red); font-weight: 700; font-size: 30px; }
  .contact-rule { width: 36px; height: 2px; background: var(--brand-red); margin: 6px 0 14px; }
  .contact-line { display: flex; align-items: center; gap: 11px; font-size: 17px; font-weight: 500; line-height: 1.9; }
  .contact-icon { width: 24px; height: 24px; flex: none; }
</style>
</head>
<body>
<main class="sheet">

  <section class="card card--front" aria-label="Card front">
    <div class="front-halo"></div>
    <div class="front-content">
      <div class="wordmark">
        <span class="wordmark-dot"></span>
        <span class="wordmark-name">Brindlewood<small>First Aid Training</small></span>
      </div>
      <p class="tagline">
        <svg class="bullet-ring" viewBox="0 0 30 30"><circle cx="15" cy="15" r="11" fill="none" stroke="#fff" stroke-width="4"/></svg>
        Onsite Training – We can come to you
      </p>
      <ul class="benefits">
        <li>Time efficient</li>
        <li>Cost effective</li>
        <li>Minimise downtime for your team</li>
      </ul>
      <div class="services">
        <p class="service"><svg class="bullet-ring" viewBox="0 0 30 30"><circle cx="15" cy="15" r="11" fill="none" stroke="#fff" stroke-width="4"/></svg>First Aid Training</p>
        <p class="service"><svg class="bullet-ring" viewBox="0 0 30 30"><circle cx="15" cy="15" r="11" fill="none" stroke="#fff" stroke-width="4"/></svg>WHS Training</p>
      </div>
    </div>
  </section>

  <section class="card card--back" aria-label="Card back">
    <div class="back-brand">
      <span class="wordmark-dot"></span>
      <span class="wordmark-name">Brindlewood<small>First Aid Training</small></span>
    </div>
    <div class="divider"></div>
    <div class="contact">
      <p class="contact-name">Daniel Hartley</p>
      <div class="contact-rule"></div>
      <p class="contact-line">
        <svg class="contact-icon" viewBox="0 0 26 26"><circle cx="13" cy="13" r="13" fill="#e2231f"/><path d="M9 7l2.5 0 1 3-1.5 1.2a8 8 0 0 0 3.8 3.8L16 13.5l3 1v2.5c0 .6-.5 1-1 1A11 11 0 0 1 8 8c0-.5.4-1 1-1z" fill="#fff"/></svg>
        0491 570 156
      </p>
      <p class="contact-line">
        <svg class="contact-icon" viewBox="0 0 26 26"><circle cx="13" cy="13" r="13" fill="#e2231f"/><rect x="6.5" y="8.5" width="13" height="9" rx="1" fill="#fff"/><path d="M7 9l6 4.5L19 9" fill="none" stroke="#e2231f" stroke-width="1.4"/></svg>
        help@brindlewoodfirstaid.com.au
      </p>
      <p class="contact-line">
        <svg class="contact-icon" viewBox="0 0 26 26"><circle cx="13" cy="13" r="13" fill="#e2231f"/><circle cx="13" cy="13" r="6.5" fill="none" stroke="#fff" stroke-width="1.5"/><ellipse cx="13" cy="13" rx="2.8" ry="6.5" fill="none" stroke="#fff" stroke-width="1.3"/><line x1="6.5" y1="13" x2="19.5" y2="13" stroke="#fff" stroke-width="1.3"/></svg>
        brindlewoodfirstaid.com.au
      </p>
    </div>
  </section>

</main>
</body>
</html>
```